Zielgruppe
Elektro und Automatisierungstechnik
Zielgruppe: Industriekunden
Aufgabenstellung
Zweiseitig farbig
Querformat 8,5*5,5cm
modernes, innovatives und zuverlässiges Unternehmen
Vorhandenes Logo muss integriert werden. Siehe Anhang

```html
<!DOCTYPE html>
<html lang="de">
<head>
<meta charset="utf-8">
<title>Kolsin Elektrotechnik – Visitenkarte</title>
<link href="https://fonts.googleapis.com/css2?family=Orbitron:wght@600&display=swap" rel="stylesheet">
<style>
  :root {
    --stage: #dcdcdc;
    --paper: #ffffff;
    --navy: #1a3a5c;
    --ink-black: #161616;
    --band-grey: #8e8e8e;
    --accent-blue-top: #2a6fb0;
    --accent-blue-bottom: #1a3a5c;
    --mint-light: #d9ece4;
    --mint-pale: #eef6f7;
  }
  * { margin: 0; padding: 0; box-sizing: border-box; }
  html, body {
    width: 1200px; height: 1200px; overflow: hidden;
    background: var(--stage);
  }
  .canvas { position: relative; width: 1200px; height: 1200px; }
  .card {
    position: absolute; left: 242px;
    width: 715px; height: 463px; overflow: hidden;
  }
  .card--front { top: 87px; background: var(--paper); }
  .card--back { top: 626px; }
  .card__shapes { position: absolute; inset: 0; }
  .card__texture {
    position: absolute; inset: 0;
    background: linear-gradient(120deg, var(--mint-light) 0%, #e6f2ef 40%, var(--mint-pale) 70%, var(--mint-pale) 100%);
  }
  .brand {
    position: absolute;
    display: flex; align-items: flex-start; gap: 14px;
    color: var(--navy);
    font-family: "Orbitron", sans-serif; font-weight: 600;
  }
  .brand__square {
    width: 24px; height: 24px; background: var(--navy); margin-top: 8px;
  }
  .brand__name { display: block; font-size: 46px; line-height: 1; letter-spacing: 1px; }
  .brand__sub { display: block; font-size: 20.5px; line-height: 1; margin-top: 10px; letter-spacing: 0.5px; }
  .card--front .brand { left: 40px; top: 128px; }
  .card--back .brand { left: 180px; top: 186px; }
  .card--back .brand__name { font-size: 51px; }
  .card--back .brand__sub { font-size: 22.5px; }
</style>
</head>
<body>
<main class="canvas">
  <section class="card card--front" aria-label="Vorderseite">
    <svg class="card__shapes" width="715" height="463" viewBox="0 0 715 463">
      <defs>
        <linearGradient id="blackFade" x1="0" y1="0" x2="0" y2="1">
          <stop offset="0" stop-color="#282828"/>
          <stop offset="1" stop-color="#090909"/>
        </linearGradient>
        <linearGradient id="blueFade" x1="0" y1="0" x2="0" y2="1">
          <stop offset="0" stop-color="var(--accent-blue-top)"/>
          <stop offset="1" stop-color="var(--accent-blue-bottom)"/>
        </linearGradient>
      </defs>
      <rect class="grey-band" x="273" y="414" width="442" height="49" fill="var(--band-grey)"/>
      <polygon class="black-panel" points="364,218 715,218 715,414 251,414" fill="url(#blackFade)"/>
      <polygon class="blue-accent" points="224,372 324,372 273,463 173,463" fill="url(#blueFade)"/>
    </svg>
    <div class="brand">
      <span class="brand__square"></span>
      <div>
        <span class="brand__name">KOLSIN</span>
        <span class="brand__sub">ELEKTROTECHNIK</span>
      </div>
    </div>
  </section>

  <section class="card card--back" aria-label="Rückseite">
    <div class="card__texture" role="img" aria-label="Heller, blasser Hintergrund mit Leiterplatten-Motiv in Mintgrün"></div>
    <div class="brand">
      <span class="brand__square"></span>
      <div>
        <span class="brand__name">KOLSIN</span>
        <span class="brand__sub">ELEKTROTECHNIK</span>
      </div>
    </div>
  </section>
</main>
</body>
</html>
```